Buch-/E-Book-Cover für Edelmetallberater
Zielgruppe
Zielgruppe sind Privatpersonen. Soll möglichst viele ansprechen, zeitgerecht und attraktiv wirken.
Ich selbst bin Edelmetallberater. Ziel ist es aufzuklären und gleichzeitig Neukunden zu gewinnen
Aufgabenstellung
Es soll attraktiv und zeitgerecht sein.
Die Bilder der Frontseite sind ein Vorschlag. Muss aber nicht so sein. Die Bilder sind von lumafoto und ich kann sie im Original liefern. Rückseite habe ich noch keinen Vorschlag. Freie Gestaltung.
Ich brauche ein fertiges Cover für ein Vendora ebook und die print Version bei Vendora

```html
<!DOCTYPE html>
<html lang="de">
<head>
<meta charset="utf-8">
<title>Wieso Sie heute Gold sichern sollten – Coverentwürfe</title>
<link rel="stylesheet" href="https://fonts.googleapis.com/css2?family=Oswald:wght@400;500;600;700&display=swap">
<style>
  :root {
    --page-bg: #ffffff;
    --blue-deep: #123f86;
    --blue-mid: #1b5cb5;
    --blue-light: #2f7ad6;
    --white: #ffffff;
    --gold-light: #ffe28a;
    --gold-mid: #e4b53f;
    --gold-dark: #a8741a;
    --gold-band: #b8902f;
    --ink-dark: #1c1406;
    --seal-dark: #2a1a08;
    --flame: #f08a1c;
    --note-green: #b9c3b0;
    --label: #111111;
  }
  * { box-sizing: border-box; margin: 0; padding: 0; }
  html, body {
    width: 1200px; height: 1200px; overflow: hidden;
    background: var(--page-bg);
    font-family: "Oswald", "Arial Narrow", sans-serif;
  }
  .stage { position: relative; width: 1200px; height: 1200px; }

  .variant-number {
    position: absolute; font-size: 44px; font-weight: 500; line-height: 1; color: var(--label);
  }
  .variant-number--one { left: 524px; top: 140px; }
  .variant-number--two { left: 1104px; top: 200px; }

  .cover {
    position: absolute; width: 520px; height: 780px; overflow: hidden;
    background: radial-gradient(ellipse at 50% 40%, var(--blue-light) 0%, var(--blue-mid) 40%, var(--blue-deep) 100%);
  }
  .cover--one { left: 50px; top: 200px; }
  .cover--two { left: 630px; top: 260px; }

  .burning-note {
    position: absolute; left: 110px; width: 300px; height: 150px;
    background:
      radial-gradient(ellipse at 50% 10%, rgba(255, 200, 60, 0.95) 0%, rgba(240, 120, 20, 0.7) 30%, transparent 55%),
      linear-gradient(180deg, var(--flame) 0%, var(--note-green) 35%, #dfe5d9 100%);
    border-radius: 6px;
  }
  .cover--one .burning-note { top: 40px; }
  .cover--two .burning-note { top: 50px; }

  .title { position: absolute; left: 0; top: 232px; width: 100%; text-align: center; line-height: 0.98; }
  .title-line { display: block; font-weight: 600; text-transform: uppercase; }
  .title-line--white { color: var(--white); text-shadow: 0 3px 6px rgba(0, 0, 0, 0.3); }
  .title-line--first { font-size: 64px; }
  .title-line--gold { font-size: 74px; }
  .title-line--last { font-size: 58px; }
  .gold-word {
    background: linear-gradient(180deg, var(--gold-light) 0%, var(--gold-mid) 50%, var(--gold-dark) 100%);
    -webkit-background-clip: text; background-clip: text; color: transparent;
  }

  .subtitle {
    position: absolute; left: 50%; transform: translateX(-50%);
    width: 400px; padding: 6px 0;
    border-top: 1px solid rgba(255, 255, 255, 0.5);
    border-bottom: 1px solid rgba(255, 255, 255, 0.5);
    color: var(--white); font-size: 17px; font-weight: 400; text-align: center; letter-spacing: 0.3px;
    white-space: nowrap;
  }
  .cover--one .subtitle { top: 448px; }
  .cover--two .subtitle { top: 456px; }

  .gold-bars { position: absolute; }
  .cover--one .gold-bars {
    left: 0; top: 505px; width: 340px; height: 185px; border-top-right-radius: 30px;
    background: radial-gradient(ellipse at 45% 45%, var(--gold-light) 0%, var(--gold-mid) 35%, var(--gold-dark) 70%, rgba(60, 40, 10, 0.9) 100%);
  }
  .cover--two .gold-bars {
    left: 130px; top: 520px; width: 250px; height: 180px; border-radius: 10px;
    background: linear-gradient(160deg, var(--gold-light) 0%, var(--gold-mid) 45%, var(--gold-dark) 100%);
  }

  .price-chart { position: absolute; left: 300px; top: 560px; width: 220px; height: 120px; }

  .seal {
    position: absolute; width: 124px; height: 124px; border-radius: 50%;
    background: radial-gradient(circle, var(--gold-light) 0%, var(--gold-mid) 60%, var(--gold-dark) 100%);
    display: flex; align-items: center; justify-content: center;
  }
  .cover--one .seal { left: 372px; top: 515px; }
  .cover--two .seal { left: 382px; top: 525px; }
  .seal-inner {
    width: 104px; height: 104px; border-radius: 50%;
    display: flex; flex-direction: column; align-items: center; justify-content: center;
    text-align: center; color: var(--ink-dark);
  }
  .cover--two .seal-inner { background: var(--seal-dark); color: var(--white); }
  .seal-heading { font-size: 15px; font-weight: 700; line-height: 1.1; }
  .seal-text { font-size: 7.5px; font-weight: 600; line-height: 1.2; }

  .author-band {
    position: absolute; left: 0; bottom: 0; width: 100%; height: 90px;
    background: linear-gradient(180deg, #d1ab52 0%, var(--gold-band) 50%, #8e6a1c 100%);
    display: flex; align-items: center; justify-content: center;
  }
  .author { font-size: 30px; font-weight: 500; letter-spacing: 6px; text-transform: uppercase; }
  .cover--one .author { color: var(--white); }
  .cover--two .author {
    position: absolute; left: 0; width: 100%; top: 722px; text-align: center;
    background: linear-gradient(180deg, var(--gold-light) 0%, var(--gold-mid) 60%, var(--gold-dark) 100%);
    -webkit-background-clip: text; background-clip: text; color: transparent;
  }
</style>
</head>
<body>
<main class="stage">
  <span class="variant-number variant-number--one">1</span>
  <span class="variant-number variant-number--two">2</span>

  <article class="cover cover--one">
    <div class="burning-note" role="img" aria-label="Brennender 100-Euro-Schein"></div>
    <h1 class="title">
      <span class="title-line title-line--white title-line--first">Wieso Sie</span>
      <span class="title-line title-line--gold"><span class="gold-word">Heute Gold</span></span>
      <span class="title-line title-line--white title-line--last">Sichern sollten</span>
    </h1>
    <p class="subtitle">IHR KLARER LEITFADEN FÜR UNRUHIGE ZEITEN</p>
    <div class="gold-bars" role="img" aria-label="Gestapelte Goldbarren"></div>
    <svg class="price-chart" viewBox="0 0 220 120" aria-hidden="true">
      <polyline points="0,100 20,92 35,98 55,80 70,86 90,70 105,76 125,55 140,62 160,40 178,48 200,25 220,18"
        fill="none" stroke="rgba(255,255,255,0.55)" stroke-width="1.5"/>
    </svg>
    <div class="seal">
      <div class="seal-inner">
        <span class="seal-heading">INKLUSIVE</span>
        <span class="seal-text">SILBER, PLATIN, PALLADIUM,<br>TECHNOLOGIEMETALLEN<br>UND<br>KRYPTOWÄHRUNGEN</span>
      </div>
    </div>
    <div class="author-band"><span class="author">Lukas Verholt</span></div>
  </article>

  <article class="cover cover--two">
    <div class="burning-note" role="img" aria-label="Brennender 100-Euro-Schein"></div>
    <h1 class="title">
      <span class="title-line title-line--white title-line--first">Wieso Sie</span>
      <span class="title-line title-line--gold"><span class="gold-word">Heute Gold</span></span>
      <span class="title-line title-line--white title-line--last">Sichern sollten</span>
    </h1>
    <p class="subtitle">IHR KLARER LEITFADEN FÜR UNRUHIGE ZEITEN</p>
    <div class="gold-bars" role="img" aria-label="Zwei Feingoldbarren zu 1000 g"></div>
    <div class="seal">
      <div class="seal-inner">
        <span class="seal-heading">INKLUSIVE</span>
        <span class="seal-text">SILBER, PLATIN, PALLADIUM,<br>TECHNOLOGIEMETALLEN<br>UND<br>KRYPTOWÄHRUNGEN</span>
      </div>
    </div>
    <span class="author">Lukas Verholt</span>
  </article>
</main>
</body>
</html>
```